Contemporary Media Company with Logo Needs Business Card Design

Need a modern card design for a full service digital media company using the logo included. Also want the info below on the card. Probably list the services on the card back to save space for the front. Want something contemporary to impress prospective clients. You may want to submit both a somewhat more conservative design, and then a more wild one.
General Info: (this phrase need not be on the card)
Tod Parvin
Founder and CEO
949-628-4513
tod@lumavantstudio.example
lumavantstudio.example
Services: (this word need not be on the card)
Content & Experience Strategy
Brand Development
Search Engine Optimization
Website Design
Website Operation
Social Media Integration
Complete Video Solutions
Industry/Entity Type
Business
Contact Information for Business Card
Tod Parvin
Founder and CEO
949-628-4513
tod@lumavantstudio.example
lumavantstudio.example
Brand Development
Website Design
Website Operation
Social Media Integration
Complete Video Solutions
Look and feel

```html
<!DOCTYPE html>
<html lang="en">
<head>
<meta charset="utf-8">
<title>Lumavant Studio – Business Card</title>
<link rel="stylesheet" href="https://fonts.googleapis.com/css2?family=Source+Sans+3:ital,wght@0,400;0,600;1,400&display=swap">
<style>
  :root {
    --orange: #ee7326;
    --grey: #6d6e70;
    --grey-light: #8a8b8d;
    --ink: #2b2b2b;
    --paper: #ffffff;
    --backdrop: #e6e6e6;
  }
  * { box-sizing: border-box; margin: 0; padding: 0; }
  html, body { width: 1105px; height: 1200px; overflow: hidden; }
  body {
    background: var(--backdrop);
    font-family: "Source Sans 3", "Segoe UI", sans-serif;
    position: relative;
  }
  .card {
    position: absolute;
    left: 62px;
    width: 980px;
    height: 560px;
    overflow: hidden;
    background: var(--paper);
  }
  .card--front { top: 30px; }
  .card--back { top: 610px; }
  .card__face {
    position: absolute;
    left: 0; top: 0;
    width: 522px;
    height: 298px;
    transform: scale(1.8774);
    transform-origin: 0 0;
  }

  /* Brand name block */
  .brand { position: absolute; display: flex; align-items: center; gap: 12px; }
  .brand__square { width: 30px; height: 30px; background: var(--orange); flex: none; }
  .brand__name {
    color: var(--grey);
    font-weight: 400;
    line-height: 1;
    text-transform: uppercase;
  }
  .brand__name span { display: block; }
  .brand__line-1 { font-size: 36px; letter-spacing: 1px; }
  .brand__line-2 { font-size: 17px; letter-spacing: 10.5px; margin-top: 4px; }

  .card--front .brand { left: 112px; top: 66px; }

  /* Person */
  .person {
    position: absolute;
    right: 318px;
    top: 180px;
    text-align: right;
  }
  .person__name {
    color: var(--orange);
    font-weight: 600;
    font-size: 17px;
    letter-spacing: 0.3px;
    text-transform: uppercase;
    line-height: 1.1;
  }
  .person__title {
    color: var(--ink);
    font-weight: 600;
    font-size: 13px;
    text-transform: uppercase;
    margin-top: 4px;
  }
  .divider {
    position: absolute;
    left: 224px; top: 169px;
    width: 1px; height: 60px;
    background: #c8c8c8;
  }

  /* Contacts */
  .contacts { position: absolute; left: 243px; top: 170px; list-style: none; }
  .contacts li {
    display: flex; align-items: center; gap: 8px;
    height: 20px;
    font-size: 13.5px;
    color: var(--ink);
  }
  .contacts svg { width: 12px; height: 12px; fill: var(--orange); flex: none; }

  /* Bottom stripe */
  .stripe { position: absolute; left: 0; top: 270px; width: 522px; height: 28px; }

  /* Back */
  .card--back .brand { left: 50%; top: 92px; transform: translateX(-50%); }
  .services {
    position: absolute;
    left: 0; right: 0; top: 212px;
    text-align: center;
    font-style: italic;
    font-size: 14.5px;
    line-height: 18px;
    color: var(--ink);
  }
  .services p { white-space: nowrap; }
  .services .sep {
    display: inline-block;
    width: 5px; height: 5px;
    background: var(--orange);
    margin: 0 4px;
    vertical-align: 3px;
  }
</style>
</head>
<body>

<section class="card card--front">
  <div class="card__face">
    <div class="brand">
      <div class="brand__square"></div>
      <div class="brand__name"><span class="brand__line-1">Lumavant</span><span class="brand__line-2">Studio</span></div>
    </div>

    <div class="person">
      <p class="person__name">Tod Parvin</p>
      <p class="person__title">Founder &amp; CEO</p>
    </div>
    <div class="divider"></div>

    <ul class="contacts">
      <li>
        <svg viewBox="0 0 24 24" aria-hidden="true"><path d="M6.6 10.8a15.1 15.1 0 0 0 6.6 6.6l2.2-2.2a1 1 0 0 1 1-.25 11.4 11.4 0 0 0 3.6.57 1 1 0 0 1 1 1V20a1 1 0 0 1-1 1A17 17 0 0 1 3 4a1 1 0 0 1 1-1h3.5a1 1 0 0 1 1 1c0 1.25.2 2.45.57 3.57a1 1 0 0 1-.25 1z"/></svg>
        949-628-4513
      </li>
      <li>
        <svg viewBox="0 0 24 24" aria-hidden="true"><path d="M2 5h20v14H2z M3 6l9 7 9-7" fill="var(--orange)"/><path d="M3 6l9 7 9-7" fill="none" stroke="#fff" stroke-width="1.6"/></svg>
        tod@lumavantstudio.example
      </li>
      <li>
        <svg viewBox="0 0 24 24" aria-hidden="true"><circle cx="12" cy="12" r="10"/><path d="M2 12h20M12 2c3 3 3 17 0 20M12 2c-3 3-3 17 0 20" fill="none" stroke="#fff" stroke-width="1.4"/></svg>
        lumavantstudio.example
      </li>
    </ul>

    <svg class="stripe" viewBox="0 0 522 28" aria-hidden="true">
      <rect x="0" y="8" width="522" height="20" fill="var(--grey)"/>
      <rect x="0" y="3" width="440" height="3.5" fill="var(--orange)"/>
      <polygon points="440,3 446,3 452,9 446,9" fill="var(--orange)"/>
      <polygon points="452,9 458,3 522,3 522,6.5 460,6.5 454,12" fill="var(--grey-light)"/>
    </svg>
  </div>
</section>

<section class="card card--back">
  <div class="card__face">
    <div class="brand">
      <div class="brand__square"></div>
      <div class="brand__name"><span class="brand__line-1">Lumavant</span><span class="brand__line-2">Studio</span></div>
    </div>

    <div class="services">
      <p>Content &amp; Experience Strategy<span class="sep"></span>Brand Development</p>
      <p>Search Engine Optimization<span class="sep"></span>Website Design<span class="sep"></span>Website Operation</p>
      <p>Social Media Integration<span class="sep"></span>Complete Video Solutions</p>
    </div>
  </div>
</section>

</body>
</html>
```